Industrial Professional Business Card Design (Vantrel Systems)

Would like professional looking business cards. Not too busy leaning towards minimal. Should have a slogan like:
"Industrial Automation and Control".

We are a tech company that programs industrial PLC computers. We also develop custom hardware solutions. Please use the logo for inspiration.

Target Market(s)

Mining, industrial, processing, automation, factory

Industry/Entity Type

Engineering

Contact Information for Business Card

Name, phone, email, website. job title.

Font styles to use
Other font styles liked:
• droid sans

Requirements
Must have
• Use colours that go well with the logo. Not too busy design.

```html
<!DOCTYPE html>
<html lang="en">
<head>
<meta charset="utf-8">
<title>Vantrel Systems — Business Card</title>
<link rel="stylesheet" href="https://fonts.googleapis.com/css2?family=Open+Sans:wght@400;600;700;800&display=swap">
<style>
  :root {
    --backdrop: #393c3f;
    --navy: #0f2533;
    --navy-deep: #0a1b26;
    --brand-blue: #1d4a6e;
    --orange: #f06a1f;
    --paper: #f3f3f3;
    --paper-light: #fbfbfb;
    --ink-light: #e9eef2;
    --ink-muted: #aab8c3;
  }
  * { box-sizing: border-box; margin: 0; padding: 0; }
  html, body {
    width: 1200px; height: 1200px; overflow: hidden;
    background: var(--backdrop);
    font-family: "Open Sans", "Droid Sans", sans-serif;
  }
  .canvas {
    position: relative; width: 1200px; height: 1200px;
  }
  .card {
    position: absolute; left: 180px; width: 840px; height: 480px;
    box-shadow: 0 24px 50px rgba(0,0,0,0.35);
    overflow: hidden;
  }

  /* Back side — contact details */
  .card-back {
    top: 80px;
    background: linear-gradient(160deg, var(--navy) 0%, var(--navy-deep) 100%);
    color: var(--ink-light);
  }
  .contact-block { position: absolute; left: 96px; top: 92px; }
  .person-name {
    font-size: 46px; font-weight: 800; letter-spacing: -0.5px; line-height: 1;
    color: #ffffff;
  }
  .person-title {
    margin-top: 6px; font-size: 12px; font-weight: 600;
    letter-spacing: 1px; text-transform: uppercase; color: var(--ink-muted);
  }
  .contact-list { margin-top: 44px; list-style: none; }
  .contact-item {
    display: flex; align-items: center; gap: 16px; margin-bottom: 16px;
  }
  .contact-icon { width: 24px; height: 24px; flex: none; }
  .contact-phone { font-size: 28px; font-weight: 400; letter-spacing: 1px; }
  .contact-email { font-size: 15px; text-transform: uppercase; letter-spacing: 0.5px; color: var(--ink-muted); }
  .website {
    position: absolute; left: 96px; bottom: 70px;
    font-size: 17px; font-weight: 600; letter-spacing: 6px;
    text-transform: uppercase; color: var(--ink-muted);
  }

  /* Front side — brand */
  .card-front {
    top: 620px;
    background: var(--paper);
    display: flex; flex-direction: column; align-items: center; justify-content: center;
  }
  .front-sheen {
    position: absolute; inset: 0; width: 100%; height: 100%;
  }
  .brand { position: relative; display: flex; align-items: center; gap: 18px; }
  .brand-dot { width: 30px; height: 30px; border-radius: 50%; background: var(--orange); }
  .brand-name {
    font-size: 62px; font-weight: 600; color: var(--brand-blue); letter-spacing: -0.5px;
  }
  .slogan {
    position: relative; margin-top: 14px;
    font-size: 17px; color: var(--brand-blue); letter-spacing: 0.3px;
  }
</style>
</head>
<body>
<main class="canvas">
  <section class="card card-back">
    <div class="contact-block">
      <h1 class="person-name">Marcos Teixeira</h1>
      <p class="person-title">Graphic Designers</p>
      <ul class="contact-list">
        <li class="contact-item">
          <svg class="contact-icon" viewBox="0 0 24 24" aria-hidden="true">
            <path fill="#f06a1f" d="M6.6 10.8a15.1 15.1 0 0 0 6.6 6.6l2.2-2.2a1 1 0 0 1 1-.25 11.4 11.4 0 0 0 3.6.57 1 1 0 0 1 1 1V20a1 1 0 0 1-1 1A17 17 0 0 1 3 4a1 1 0 0 1 1-1h3.5a1 1 0 0 1 1 1c0 1.25.2 2.45.57 3.57a1 1 0 0 1-.25 1z"/>
          </svg>
          <span class="contact-phone">+55 19 4021 7736</span>
        </li>
        <li class="contact-item">
          <svg class="contact-icon" viewBox="0 0 24 24" aria-hidden="true">
            <rect x="2" y="5" width="20" height="14" fill="#f06a1f"/>
            <path d="M2 5l10 8 10-8" fill="none" stroke="#0f2533" stroke-width="1.6"/>
          </svg>
          <span class="contact-email">contact@vantrelsystems.com</span>
        </li>
      </ul>
    </div>
    <p class="website">www.vantrelsystems.com</p>
  </section>

  <section class="card card-front">
    <svg class="front-sheen" viewBox="0 0 840 480" preserveAspectRatio="none" aria-hidden="true">
      <path d="M150 0 C 170 220, 330 400, 640 480 L 840 480 L 840 0 Z" fill="#fbfbfb"/>
    </svg>
    <div class="brand">
      <span class="brand-dot"></span>
      <span class="brand-name">Vantrel Systems</span>
    </div>
    <p class="slogan">Industrial Automation and Control</p>
  </section>
</main>
</body>
</html>
```